Mexican Restaurant needs a new Menu Design

Mexican restaurant LAS TORTUGAS is renewing its menu, so we need something new.
Since our inception we have given the task of rescuing ingredients, recipes, and traditional and representatives dishes of the culinary techniques of yesteryear.
We are the only restaurant in Guadalajara that manufactures its own dairy natural as fresh cheese, the cream and our already well-known and traditional jocoqui. In addition, we produce organic ranch egg and are currently in the development of organic vegetables cultivated on the slopes of the old Hill which gives our plants benefit from an exceptional microclimate.
Find more information about the restaurant in www.lastortugasfonda.example.
The menu needs to have the full list of products with the prices, some phrases that speak of the philosophy of the ranch-style-living, photos.
We need the cover, back cover and interiors.
Updates
Thank you so much for the proposals you have submitted for the menu design. We are looking them carefully.
Thank you very much for taking your time to design a proposal for our menu!!!
Target Market(s)
The target is very wide (28-40 yrs.): Young executives, Young families, Housewives.
Industry/Entity Type
Restaurant
Look and feel
Each slider illustrates characteristics of the customer's brand and the style your logo design should communicate.

```html
<!DOCTYPE html>
<html lang="en">
<head>
<meta charset="utf-8">
<title>Las Tortugas – Menu Pages</title>
<link href="https://fonts.googleapis.com/css2?family=Rye&family=Archivo+Narrow:wght@400;700&family=Special+Elite&display=swap" rel="stylesheet">
<style>
  :root{
    --backdrop:#1d1d1d;
    --wood-dark:#7d412c;
    --wood-mid:#a15a3d;
    --wood-light:#b36c4c;
    --wood-seam:#2e1811;
    --paper:#ece3cf;
    --paper-edge:#d6c8a8;
    --red:#c8323a;
    --red-deep:#a9262d;
    --ink:#3a2a22;
    --cream:#f3e9d6;
    --green:#8a9a3c;
    --food:#d98a4a;
    --food-dark:#9c4b2a;
  }
  *{box-sizing:border-box;margin:0;padding:0}
  html,body{width:1200px;height:969px;overflow:hidden}
  body{
    position:relative;
    background:radial-gradient(ellipse at 50% 40%,#2a2a2a 0%,var(--backdrop) 70%,#111 100%);
    font-family:"Archivo Narrow",Arial,sans-serif;
  }
  .page{position:absolute;overflow:hidden;box-shadow:0 6px 18px rgba(0,0,0,.6)}
  .wood{
    background:
      repeating-linear-gradient(to bottom,
        var(--wood-dark) 0,var(--wood-mid) 30px,var(--wood-light) 55px,var(--wood-mid) 88px,
        var(--wood-seam) 90px,var(--wood-seam) 94px);
    background-position:0 -14px;
  }
  .brand{
    position:absolute;display:flex;align-items:center;gap:6px;
    color:var(--cream);font-weight:700;letter-spacing:.06em;white-space:nowrap;
    transform:translateX(-50%);
  }
  .brand-mark{display:block;background:var(--red);border:1px solid var(--cream)}
  .brand--large{font-size:15px}
  .brand--large .brand-mark{width:12px;height:12px}
  .brand--small{font-size:9px}
  .brand--small .brand-mark{width:8px;height:8px}

  .tag{
    position:absolute;display:flex;align-items:center;justify-content:center;
    font-family:"Rye",serif;font-size:13px;letter-spacing:.03em;
    box-shadow:0 2px 6px rgba(0,0,0,.5);
  }
  .tag--paper{background:linear-gradient(180deg,var(--paper),var(--paper-edge));color:var(--red)}
  .tag--red{background:linear-gradient(180deg,var(--red),var(--red-deep));color:var(--cream)}

  .back-note{
    position:absolute;left:40px;right:40px;color:var(--cream);opacity:.85;
    font-size:5px;line-height:7px;text-align:center;
  }

  .sheet{position:absolute;top:0;bottom:0;box-shadow:2px 0 8px rgba(0,0,0,.5)}
  .sheet--paper{background:radial-gradient(ellipse at 50% 40%,#f3ecdb 0%,var(--paper) 60%,var(--paper-edge) 100%)}
  .sheet--red{background:radial-gradient(ellipse at 50% 40%,#cf3b41 0%,var(--red) 60%,var(--red-deep) 100%)}

  .quote{
    position:absolute;left:52px;right:20px;top:18px;
    font-size:6px;line-height:8px;font-weight:700;font-style:italic;color:var(--ink);text-align:center;
  }
  .story-photo{position:absolute;left:42px;top:27px;width:86px;height:65px;
    background:linear-gradient(180deg,#e9e4dc 0%,#b83a3a 55%,#5a5a52 100%);border:2px solid var(--cream)}
  .story{
    position:absolute;left:140px;right:10px;top:30px;
    font-family:"Special Elite",monospace;font-size:5px;line-height:7.5px;
    text-transform:uppercase;color:var(--cream);
  }
  .menu-frame{position:absolute;border:1px dotted rgba(90,70,50,.6)}
  .sheet--red .menu-frame{border-color:rgba(243,233,214,.7)}
  .section-title{
    position:absolute;font-family:"Rye",serif;font-size:11px;color:var(--green);
    padding-right:4px;
  }
  .sheet--paper .section-title{background:var(--paper)}
  .sheet--red .section-title{color:var(--cream);background:var(--red)}
  .menu-list{position:absolute;left:18px;right:8px;list-style:none}
  .item{display:flex;gap:9px;height:32px;align-items:flex-start}
  .item-photo{flex:none;width:32px;height:28px;border:2px solid #fff;border-radius:2px;
    background:radial-gradient(circle at 50% 50%,var(--food) 0%,var(--food-dark) 80%)}
  .item-name{font-size:8.5px;font-weight:700;color:var(--red);line-height:11px;margin-top:2px;white-space:nowrap}
  .item-name .price{color:var(--ink)}
  .sheet--red .item-name{color:var(--cream)}
  .sheet--red .item-name .price{color:#1a1a1a}
  .item-desc{font-size:4.4px;line-height:5.5px;color:#5a4a40;max-width:130px}
  .sheet--red .item-desc{color:#f3d3cc}
</style>
</head>
<body>

<!-- Breakfast front cover -->
<section class="page wood" style="left:118px;top:91px;width:283px;height:396px" role="img" aria-label="Wooden plank background">
  <div class="brand brand--large" style="left:141px;top:122px"><span class="brand-mark"></span>LAS TORTUGAS</div>
  <div class="tag tag--paper" style="left:17px;top:356px;width:248px;height:40px">Breakfast Menu</div>
</section>

<!-- Breakfast interior -->
<section class="page wood" style="left:440px;top:91px;width:280px;height:396px" role="img" aria-label="Wooden plank background">
  <div class="sheet sheet--paper" style="left:18px;width:248px">
    <p class="quote">"Lorem ipsum. Proin gravida nibh vel velit auctor aliquet. Aenean sollicitudin, lorem quis bibendum auctor, nisi elit consequat ipsum, nec sagittis sem nibh id elit."</p>
    <div class="menu-frame" style="left:24px;right:12px;top:52px;bottom:28px"></div>
    <h2 class="section-title" style="left:27px;top:46px">Del Rancho</h2>
    <ul class="menu-list" style="left:42px;top:68px">
      <li class="item"><span class="item-photo" role="img" aria-label="Plated breakfast dish"></span><div><h3 class="item-name">Huevos Rancheros <span class="price">| 4.30 €</span></h3><p class="item-desc">Ranch eggs on warm tortillas with red salsa, fresh cheese, cream and beans.</p></div></li>
      <li class="item"><span class="item-photo" role="img" aria-label="Plated breakfast dish"></span><div><h3 class="item-name">Molletes Gratinados con Natas <span class="price">| 4.30 €</span></h3><p class="item-desc">Toasted bread with beans, melted cheese, fresh cream and pico de gallo.</p></div></li>
      <li class="item"><span class="item-photo" role="img" aria-label="Plated breakfast dish"></span><div><h3 class="item-name">Enfrijoladas Rojas <span class="price">| 4.30 €</span></h3><p class="item-desc">Soft tortillas in bean sauce with fresh cheese, cream and onion.</p></div></li>
      <li class="item"><span class="item-photo" role="img" aria-label="Plated breakfast dish"></span><div><h3 class="item-name">Quesadillas de Calabacita <span class="price">| 4.30 €</span></h3><p class="item-desc">Handmade corn tortillas with squash, fresh cheese and green salsa.</p></div></li>
      <li class="item"><span class="item-photo" role="img" aria-label="Plated breakfast dish"></span><div><h3 class="item-name">Huevos Gratinados <span class="price">| 4.30 €</span></h3><p class="item-desc">Baked ranch eggs with melted cheese, cream and a side of beans.</p></div></li>
      <li class="item"><span class="item-photo" role="img" aria-label="Plated breakfast dish"></span><div><h3 class="item-name">Enchiladas Verdes de Pollo <span class="price">| 4.30 €</span></h3><p class="item-desc">Chicken rolled in tortillas with green salsa, cream and fresh cheese.</p></div></li>
      <li class="item"><span class="item-photo" role="img" aria-label="Plated breakfast dish"></span><div><h3 class="item-name">Tamales con Mole de Olla <span class="price">| 4.30 €</span></h3><p class="item-desc">Steamed corn tamales under house mole with sesame and fresh cream.</p></div></li>
      <li class="item"><span class="item-photo" role="img" aria-label="Plated breakfast dish"></span><div><h3 class="item-name">Tacos de Guisado <span class="price">| 4.30 €</span></h3><p class="item-desc">Three soft tacos with the stew of the day, onion and cilantro.</p></div></li>
      <li class="item"><span class="item-photo" role="img" aria-label="Plated breakfast dish"></span><div><h3 class="item-name">Huevos a la Diabla <span class="price">| 4.30 €</span></h3><p class="item-desc">Ranch eggs in a hot chile sauce with beans and warm tortillas.</p></div></li>
    </ul>
  </div>
</section>

<!-- Breakfast back cover -->
<section class="page wood" style="left:755px;top:91px;width:282px;height:396px" role="img" aria-label="Wooden plank background">
  <div class="tag tag--paper" style="left:22px;top:0;width:243px;height:38px">Breakfast Menu</div>
  <div class="brand brand--small" style="left:141px;top:284px"><span class="brand-mark"></span>LAS TORTUGAS</div>
  <p class="back-note" style="top:331px">Ranch cooking from old family recipes, with our own cheese, cream and eggs, served fresh every morning for you and yours.</p>
</section>

<!-- Lunch front cover -->
<section class="page wood" style="left:118px;top:521px;width:283px;height:394px" role="img" aria-label="Wooden plank background">
  <div class="brand brand--large" style="left:141px;top:120px"><span class="brand-mark"></span>LAS TORTUGAS</div>
  <div class="tag tag--red" style="left:17px;top:354px;width:248px;height:40px">Lunch Menu</div>
</section>

<!-- Lunch interior -->
<section class="page wood" style="left:440px;top:521px;width:280px;height:394px" role="img" aria-label="Wooden plank background">
  <div class="sheet sheet--red" style="left:0;width:266px">
    <div class="story-photo" role="img" aria-label="Photo of the restaurant facade"></div>
    <p class="story">We make our own fresh cheese, cream and jocoqui by hand every day, raise our ranch eggs outdoors and grow organic vegetables on the hillside behind the kitchen, so that every plate on this table tastes of slow, honest ranch living.</p>
    <div class="menu-frame" style="left:42px;right:12px;top:123px;bottom:28px"></div>
    <h2 class="section-title" style="left:45px;top:116px">Del Rancho</h2>
    <ul class="menu-list" style="left:60px;top:138px">
      <li class="item"><span class="item-photo" role="img" aria-label="Plated lunch dish"></span><div><h3 class="item-name">Huevos Rancheros <span class="price">| 4.30 €</span></h3><p class="item-desc">Ranch eggs on warm tortillas with red salsa, fresh cheese, cream and beans.</p></div></li>
      <li class="item"><span class="item-photo" role="img" aria-label="Plated lunch dish"></span><div><h3 class="item-name">Molletes Gratinados con Natas <span class="price">| 4.30 €</span></h3><p class="item-desc">Toasted bread with beans, melted cheese, fresh cream and pico de gallo.</p></div></li>
      <li class="item"><span class="item-photo" role="img" aria-label="Plated lunch dish"></span><div><h3 class="item-name">Enfrijoladas Rojas <span class="price">| 4.30 €</span></h3><p class="item-desc">Soft tortillas in bean sauce with fresh cheese, cream and onion.</p></div></li>
      <li class="item"><span class="item-photo" role="img" aria-label="Plated lunch dish"></span><div><h3 class="item-name">Quesadillas de Calabacita <span class="price">| 4.30 €</span></h3><p class="item-desc">Handmade corn tortillas with squash, fresh cheese and green salsa.</p></div></li>
      <li class="item"><span class="item-photo" role="img" aria-label="Plated lunch dish"></span><div><h3 class="item-name">Huevos Gratinados <span class="price">| 4.30 €</span></h3><p class="item-desc">Baked ranch eggs with melted cheese, cream and a side of beans.</p></div></li>
      <li class="item"><span class="item-photo" role="img" aria-label="Plated lunch dish"></span><div><h3 class="item-name">Enchiladas Verdes de Pollo <span class="price">| 4.30 €</span></h3><p class="item-desc">Chicken rolled in tortillas with green salsa, cream and fresh cheese.</p></div></li>
      <li class="item"><span class="item-photo" role="img" aria-label="Plated lunch dish"></span><div><h3 class="item-name">Tamales con Mole de Olla <span class="price">| 4.30 €</span></h3><p class="item-desc">Steamed corn tamales under house mole with sesame and fresh cream.</p></div></li>
    </ul>
  </div>
</section>

<!-- Lunch back cover -->
<section class="page wood" style="left:755px;top:521px;width:282px;height:394px" role="img" aria-label="Wooden plank background">
  <div class="tag tag--red" style="left:17px;top:0;width:248px;height:40px">Lunch Menu</div>
  <div class="brand brand--small" style="left:141px;top:290px"><span class="brand-mark"></span>LAS TORTUGAS</div>
  <p class="back-note" style="top:334px">Ranch cooking from old family recipes, with our own cheese, cream and eggs, served fresh every afternoon for you and yours.</p>
</section>

</body>
</html>
```